Stationary and Business Card for a Car leasing company
Brivo Motor Rentals LLC
Modern
Owen Ferrick
President
418 Halden Ridge Road
Pallisburg, NY 10847
oferrick@brivomotorrentals.com
Change the title of the "Cell Phone" to phone. There are two contact phone numbers.
** want a plain business card (generic) with no personal information - just business name, contact address and phone numbers

```html
<!DOCTYPE html>
<html lang="en">
<head>
<meta charset="utf-8">
<title>Brivo Motor Rentals LLC — Business Card</title>
<link rel="stylesheet" href="https://fonts.googleapis.com/css2?family=Open+Sans:wght@400;600;800&display=swap">
<style>
  :root {
    --page-bg: #e4e6ea;
    --brand-blue: #1d3fd6;
    --brand-blue-deep: #10269a;
    --brand-green: #25b43c;
    --card-white: #ffffff;
    --ink-light: #ffffff;
    --ink-soft: #d8def8;
  }
  * { margin: 0; padding: 0; box-sizing: border-box; }
  html, body { width: 1200px; height: 895px; overflow: hidden; }
  body {
    background: var(--page-bg);
    font-family: "Open Sans", Arial, sans-serif;
    position: relative;
  }
  .card {
    position: absolute;
    width: 540px;
    height: 309px;
    top: 293px;
    overflow: hidden;
    box-shadow: 0 6px 18px rgba(0,0,0,0.18);
  }
  .card--contact { left: 40px; background: var(--card-white); }
  .card--brand {
    left: 620px;
    background: radial-gradient(ellipse at 55% 40%, var(--brand-blue) 0%, var(--brand-blue-deep) 100%);
    display: flex; flex-direction: column; align-items: center; justify-content: center;
  }
  .card-curve { position: absolute; inset: 0; width: 100%; height: 100%; }
  .holder { position: absolute; left: 24px; top: 22px; color: var(--ink-light); }
  .holder-name { font-size: 15px; font-weight: 600; }
  .holder-title { font-size: 11px; color: var(--ink-soft); margin-top: 2px; }
  .contact-list { position: absolute; left: 24px; top: 112px; list-style: none; }
  .contact-item {
    display: flex; align-items: center; gap: 8px;
    color: var(--ink-light); font-size: 10.5px; line-height: 1.3;
    margin-bottom: 6px;
  }
  .contact-icon { width: 15px; height: 15px; flex: none; }
  .brand-block { position: absolute; left: 300px; top: 0; width: 240px; height: 309px;
    display: flex; flex-direction: column; align-items: center; justify-content: center; text-align: center; }
  .brand-mark { display: flex; align-items: center; gap: 8px; }
  .brand-dot { width: 14px; height: 14px; border-radius: 50%; background: var(--brand-green); flex: none; }
  .brand-name { font-size: 19px; font-weight: 800; color: var(--brand-blue); line-height: 1.15; }
  .brand-tagline { font-size: 10px; color: var(--brand-blue-deep); margin-top: 8px; font-weight: 600; }
  .card--brand .brand-name { color: var(--ink-light); font-size: 28px; }
  .card--brand .brand-tagline { color: var(--ink-soft); font-size: 12px; }
  .card--brand .brand-dot { width: 18px; height: 18px; }
</style>
</head>
<body>

<section class="card card--contact" aria-label="Business card, contact side">
  <svg class="card-curve" viewBox="0 0 540 309" preserveAspectRatio="none" aria-hidden="true">
    <defs>
      <linearGradient id="panelBlue" x1="0" y1="0" x2="1" y2="1">
        <stop offset="0" stop-color="#2347e0"/>
        <stop offset="1" stop-color="#132a9e"/>
      </linearGradient>
    </defs>
    <path d="M0 0 H290 C262 90 258 200 272 309 H0 Z" fill="var(--brand-green)" transform="translate(14 0)"/>
    <path d="M0 0 H290 C262 90 258 200 272 309 H0 Z" fill="#ffffff" transform="translate(7 0)"/>
    <path d="M0 0 H290 C262 90 258 200 272 309 H0 Z" fill="url(#panelBlue)"/>
  </svg>

  <div class="holder">
    <p class="holder-name">Owen Ferrick</p>
    <p class="holder-title">President</p>
  </div>

  <ul class="contact-list">
    <li class="contact-item">
      <svg class="contact-icon" viewBox="0 0 16 16" aria-hidden="true"><circle cx="8" cy="8" r="8" fill="#fff" opacity=".25"/><path d="M8 3.5a2.8 2.8 0 0 0-2.8 2.8C5.2 8.6 8 12.5 8 12.5s2.8-3.9 2.8-6.2A2.8 2.8 0 0 0 8 3.5Zm0 3.8a1 1 0 1 1 0-2 1 1 0 0 1 0 2Z" fill="#fff"/></svg>
      <span>418 Halden Ridge Road<br>Pallisburg, NY 10847</span>
    </li>
    <li class="contact-item">
      <svg class="contact-icon" viewBox="0 0 16 16" aria-hidden="true"><circle cx="8" cy="8" r="8" fill="#fff" opacity=".25"/><path d="M5.2 4h1.6l.8 2-1 .8a5 5 0 0 0 2.6 2.6l.8-1 2 .8v1.6c0 .6-.5 1.1-1.1 1.1A6.9 6.9 0 0 1 4.1 5.1C4.1 4.5 4.6 4 5.2 4Z" fill="#fff"/></svg>
      <span>845-555-0142</span>
    </li>
    <li class="contact-item">
      <svg class="contact-icon" viewBox="0 0 16 16" aria-hidden="true"><circle cx="8" cy="8" r="8" fill="#fff" opacity=".25"/><path d="M5.2 4h1.6l.8 2-1 .8a5 5 0 0 0 2.6 2.6l.8-1 2 .8v1.6c0 .6-.5 1.1-1.1 1.1A6.9 6.9 0 0 1 4.1 5.1C4.1 4.5 4.6 4 5.2 4Z" fill="#fff"/></svg>
      <span>845-555-0187</span>
    </li>
    <li class="contact-item">
      <svg class="contact-icon" viewBox="0 0 16 16" aria-hidden="true"><circle cx="8" cy="8" r="8" fill="#fff" opacity=".25"/><rect x="4" y="5" width="8" height="6" rx="1" fill="none" stroke="#fff"/><path d="M4.3 5.4 8 8.3l3.7-2.9" fill="none" stroke="#fff"/></svg>
      <span>oferrick@brivomotorrentals.com</span>
    </li>
    <li class="contact-item">
      <svg class="contact-icon" viewBox="0 0 16 16" aria-hidden="true"><circle cx="8" cy="8" r="8" fill="#fff" opacity=".25"/><circle cx="8" cy="8" r="4" fill="none" stroke="#fff"/><path d="M4 8h8M8 4c-1.6 2.4-1.6 5.6 0 8M8 4c1.6 2.4 1.6 5.6 0 8" fill="none" stroke="#fff" stroke-width=".8"/></svg>
      <span>www.brivomotorrentals.com</span>
    </li>
  </ul>

  <div class="brand-block">
    <div class="brand-mark">
      <span class="brand-dot" aria-hidden="true"></span>
      <p class="brand-name">Brivo Motor<br>Rentals LLC</p>
    </div>
    <p class="brand-tagline">Turnkey livery vehicles - lease to own</p>
  </div>
</section>

<section class="card card--brand" aria-label="Business card, brand side">
  <div class="brand-mark">
    <span class="brand-dot" aria-hidden="true"></span>
    <p class="brand-name">Brivo Motor Rentals LLC</p>
  </div>
  <p class="brand-tagline">Turnkey livery vehicles - lease to own</p>
</section>

</body>
</html>
```